Velmora 52

The existing website (velmora multihull.com) needs to be simplified.

Need a more restrained style ... lots of white background, fine grey extended titles, a spot of ultramarine or red here and there, one long page for ease of scrolling on a phone.

Need extra days to review

```html
<!DOCTYPE html>
<html lang="en">
<head>
<meta charset="utf-8">
<title>Velmora 52 – Build A 60-Foot Ocean Cruising Catamaran</title>
<link rel="stylesheet" href="https://fonts.googleapis.com/css2?family=Montserrat:wght@500;600;700&family=Raleway:wght@300;400;500;600&display=swap">
<style>
:root{
  --ultramarine:#1033f2;
  --title-grey:#8a8a8e;
  --ink:#3a3a3a;
  --soft-ink:#5a5a5e;
  --panel-grey:#f3f2f2;
  --line-grey:#d6d6d8;
  --white:#ffffff;
}
*{margin:0;padding:0;box-sizing:border-box}
html,body{width:1200px;height:4950px;overflow:hidden}
body{font-family:"Raleway",sans-serif;color:var(--ink);background:var(--white);position:relative}
section,header,footer{position:absolute;left:0;width:1200px}
.abs{position:absolute}
.site-header{top:0;height:115px;background:var(--white)}
.brand{left:110px;top:46px;font-family:"Raleway",sans-serif;font-weight:600;font-size:29px;color:var(--ultramarine)}
.hero{top:115px;height:566px;background:linear-gradient(135deg,#1d4d6b 0%,#0e3552 35%,#123a73 60%,#0b2b58 100%)}
.hero-boat{left:620px;top:0;width:580px;height:566px;background:radial-gradient(ellipse at 55% 55%,rgba(170,178,185,.55) 0%,rgba(60,70,85,.25) 45%,rgba(0,0,0,0) 70%)}
.hero-title{left:114px;top:180px;font-weight:300;font-size:43px;line-height:44px;color:var(--white)}
.btn-primary{left:112px;top:295px;width:220px;height:37px;background:var(--ultramarine);color:var(--white);border-radius:4px;font-family:"Montserrat",sans-serif;font-weight:600;font-size:11px;line-height:37px;text-align:center;letter-spacing:.3px}
.section-title{width:1200px;left:0;text-align:center;font-weight:300;font-size:40px;letter-spacing:7px;color:var(--title-grey)}
.title-rule{left:570px;width:60px;height:2px;background:var(--ultramarine)}
.hulls{top:681px;height:396px}
.hulls .section-title{top:125px}
.hulls .title-rule{top:192px}
.lead{width:1200px;left:0;top:222px;text-align:center;font-family:"Montserrat",sans-serif;font-weight:700;font-size:27px;letter-spacing:4px;color:#2a2a2a}
.intro{left:240px;top:288px;width:720px;text-align:center;font-size:13px;line-height:17px}
.wing{top:1077px;height:928px;background:var(--panel-grey)}
.wing .section-title{top:82px}
.wing .title-rule{top:155px}
.photo{display:block}
.wing-photo{left:110px;top:203px;width:965px;height:468px;background:linear-gradient(180deg,#b7b0a6 0%,#9b8c78 45%,#7c6a55 75%,#a8a29a 100%)}
.body-copy{font-size:12.5px;line-height:15px;color:var(--ink)}
.body-copy p{margin-bottom:18px}
.wing-copy{left:110px;top:713px;width:965px}
.quote-band{top:2005px;height:437px;background:var(--white);border-top:1px solid var(--line-grey);border-bottom:1px solid var(--line-grey)}
.quote{width:1200px;left:0;top:100px;text-align:center;font-family:"Montserrat",sans-serif;font-weight:600;font-size:36px;line-height:46px;color:var(--soft-ink)}
.quote-cite{width:1200px;left:0;top:283px;text-align:center;font-size:24px;font-weight:300;letter-spacing:5px;color:var(--title-grey)}
.construction{top:2442px;height:836px}
.construction .section-title{top:88px}
.construction .title-rule{top:158px}
.construction-copy{left:120px;top:210px;width:443px;text-align:justify;font-size:12px;line-height:14px}
.construction-photo{left:610px;top:208px;width:461px;height:507px;background:linear-gradient(160deg,#d7d3cc 0%,#a7a198 45%,#8c857b 70%,#c8c4bd 100%)}
.bridge{top:3278px;height:517px;background:var(--panel-grey)}
.bridge-photo{left:186px;top:65px;width:273px;height:364px;background:linear-gradient(180deg,#6c8a5a 0%,#8b9b86 35%,#d9dcd8 60%,#5c7048 100%)}
.bridge-title{left:535px;top:100px;font-weight:300;font-size:40px;letter-spacing:7px;color:var(--title-grey)}
.bridge .title-rule{left:537px;top:168px}
.bridge-copy{left:537px;top:220px;width:440px;font-size:13px;line-height:16px}
.bridge-copy p{margin-bottom:18px}
.specs{top:3795px;height:775px}
.specs .section-title{top:90px}
.specs .title-rule{top:158px}
.spec-head{left:126px;height:30px;background:var(--ultramarine);color:var(--white);font-family:"Montserrat",sans-serif;font-weight:700;font-size:18px;letter-spacing:3.5px;line-height:30px;padding-left:16px}
.spec-rows{left:126px;font-size:13px}
.spec-row{display:flex;height:24px;line-height:24px}
.spec-row .k{width:262px;padding-left:2px;font-family:"Montserrat",sans-serif;font-weight:500;font-size:13px;border-right:1px solid #bfbfbf}
.spec-row .v{padding-left:10px}
.spec-drawing{left:610px;top:295px;width:470px;height:350px;background:radial-gradient(ellipse at 50% 40%,#c4c8cc 0%,#9aa1a7 35%,rgba(255,255,255,0) 68%)}
.cta{top:4570px;height:345px;background:var(--panel-grey)}
.cta-text{width:1200px;left:0;top:82px;text-align:center;font-size:26px;font-weight:300;line-height:31px;color:var(--soft-ink)}
.cta-email{width:1200px;left:0;top:183px;text-align:center;font-family:"Montserrat",sans-serif;font-weight:700;font-size:31px;color:var(--ultramarine)}
.btn-light{left:530px;top:238px;width:136px;height:37px;background:var(--ultramarine);color:var(--white);font-family:"Montserrat",sans-serif;font-weight:600;font-size:10px;text-align:center;line-height:37px}
.site-footer{top:4915px;height:35px;background:var(--white);border-top:1px solid var(--line-grey);text-align:center;color:var(--title-grey);font-size:12px;line-height:35px}
</style>
</head>
<body>
<header class="site-header">
  <div class="abs brand">Velmora 52</div>
</header>

<section class="hero">
  <div class="abs hero-boat" role="img" aria-label="Rendering of the catamaran with its wing mast, seen from above over the sea"></div>
  <h1 class="abs hero-title">Build A 60-Foot Ocean<br>Cruising Catamaran</h1>
  <div class="abs btn-primary">MYBOAT@VELMORA52.COM</div>
</section>

<section class="hulls">
  <h2 class="abs section-title">Hulls</h2>
  <div class="abs title-rule"></div>
  <p class="abs lead">A NEW WAY TO BUILD A BIG CATAMARAN</p>
  <p class="abs intro">The Velmora Catamaran is a stunning 18+ metre (62 feet) ocean sail boat that you can build yourself for under $200,000. This beautiful twin hulled catamaran is light, strong and stable with superb upwind performance, advanced aerodynamics with minimal fairing, and an easy build methodology.</p>
</section>

<section class="wing">
  <h2 class="abs section-title">Wing Mast</h2>
  <div class="abs title-rule"></div>
  <div class="abs photo wing-photo" role="img" aria-label="Photo of the wing mast under construction on its ribs in the workshop"></div>
  <div class="abs body-copy wing-copy">
    <p>The 20 metre rotating wing mast is built by bonding layers of carbon fibre over a light weight ply and wood form.</p>
    <p>The shape of the mast is controlled by 40 ribs. They are all slightly different because the mast tapers towards the top.  These ribs are cut from one sheet of ply.</p>
    <p>Inside the form work there are conduits for halyards and cables. The conduits lead to sheave boxes at points up the mast.</p>
    <p>The mast sits on a spherical roller thrust bearing. The bearing allows halyards to pass through to elctric winches built into the main cross beam that supports the mast.</p>
  </div>
</section>

<section class="quote-band">
  <blockquote class="abs quote">Those who fall in love<br>with practice without science are like a sailor<br>who steers a ship without a helm or compass ...</blockquote>
  <p class="abs quote-cite">- Ottavio Renzi</p>
</section>

<section class="construction">
  <h2 class="abs section-title">Construction Technique</h2>
  <div class="abs title-rule"></div>
  <div class="abs body-copy construction-copy">
    <p>At first we agonised over various methods full hull building. Strip planking, balsa core, foam core. Should we laminate the epoxy and glass into a female mold or over a male mold.</p>
    <p>Building a mold, also known as a plug, would be a lot of work – and we would need two – one for each hull – they are mirror opposites.</p>
    <p>Then came the inspiration – the male mold, the plug, would form a permanent part of the hulls. And it would stiffen the outer surface. This made a lot of sense because the outer surface is in compression when punched by a wave, and thin laminate can buckle – but not if it is kept straight.</p>
    <p>So we made a thin plywood shell formed over 35 CNC cut temporary frames spaced half a metre apart. The resulting shell was very accurate, not much fairing was needed. The scarf joined ply sheets were thoroughly bonded together with triple coats of epoxy.</p>
    <p>After the outer ply surface was laminated with lateral, longitudinal and bi-axial layers, we rolled the hull, removed the frames and vacuum bagged a foam core to the inside surface of the ply.</p>
    <p>Finally we laminated over the foam, again using a vacuum bag to get a thorough bond, with long, lateral and bi-axial glass.</p>
    <p>It took only about ten weeks to build our first hull. And the temporary frames could be flipped around and reused again to make the mirror opposite hull.</p>
  </div>
  <div class="abs photo construction-photo" role="img" aria-label="Photo of builders working on a hull shell in the workshop"></div>
</section>

<section class="bridge">
  <div class="abs photo bridge-photo" role="img" aria-label="Photo of a roof module being lifted into position outdoors"></div>
  <h2 class="abs bridge-title">Bridge Deck</h2>
  <div class="abs title-rule"></div>
  <div class="abs bridge-copy">
    <p style="font-weight:500">The bridge deck is assembled from individually built modules:<br>Floors, Cross beam and Roof</p>
    <p>Each module can be handled relatively easily and the precision building technique guarantees everything fits together perfectly</p>
    <p>The picture shows a roof module being lifted into position</p>
  </div>
</section>

<section class="specs">
  <h2 class="abs section-title">Specifications</h2>
  <div class="abs title-rule"></div>
  <div class="abs spec-drawing" role="img" aria-label="Cutaway drawing of the catamaran showing hulls and interior"></div>
  <div class="abs spec-head" style="top:195px;width:952px">DIMENTIONS</div>
  <div class="abs spec-rows" style="top:232px">
    <div class="spec-row"><span class="k">Length overall</span><span class="v">18.6m / 61 feet</span></div>
    <div class="spec-row"><span class="k">Length waterline</span><span class="v">18.5 m</span></div>
    <div class="spec-row"><span class="k">Beam</span><span class="v">8.8 m</span></div>
    <div class="spec-row"><span class="k">Draft</span><span class="v">0.5m boards up / 3 m boards down</span></div>
    <div class="spec-row"><span class="k">Bridge deck clearance (unloaded)</span><span class="v">1 m</span></div>
    <div class="spec-row"><span class="k">Mast height above waterline</span><span class="v">24 m</span></div>
  </div>
  <div class="abs spec-head" style="top:388px;width:489px">SAIL AREAS</div>
  <div class="abs spec-rows" style="top:425px">
    <div class="spec-row"><span class="k">Sail Area – Mainsail</span><span class="v">106 m²</span></div>
    <div class="spec-row"><span class="k">Sail Area–Reacher</span><span class="v">83 m²</span></div>
    <div class="spec-row"><span class="k">Sail Area–Jib</span><span class="v">36 m²</span></div>
  </div>
  <div class="abs spec-head" style="top:523px;width:609px">ELECTRIC PROPULSION</div>
  <div class="abs spec-rows" style="top:558px">
    <div class="spec-row"><span class="k" style="padding-left:16px">Engines</span><span class="v">Peak power 50 kW brushless</span></div>
    <div class="spec-row"><span class="k"></span><span class="v">DC motor each hull - total 100 kW</span></div>
    <div class="spec-row"><span class="k" style="padding-left:16px">Fresh water (2x400 L tanks)</span><span class="v">800 litres</span></div>
    <div class="spec-row"><span class="k" style="padding-left:16px">Diesel (2x400 L tanks)</span><span class="v">800 litres</span></div>
    <div class="spec-row"><span class="k" style="padding-left:16px">Unloaded displacement</span><span class="v">11,000 kg</span></div>
  </div>
</section>

<section class="cta">
  <p class="abs cta-text">For more information on how you can build this<br>beautiful ocean cruising sail boat for under $200,000, email<br>The Velmora Catamaran On</p>
  <p class="abs cta-email">myboat@velmora52.com</p>
  <div class="abs btn-light">CONTACT US</div>
</section>

<footer class="site-footer">Copyright 2021@the velmora multihull</footer>
</body>
</html>
```